Visitenkarten für Psychotherapeutin
Zielgruppe
Ich war Psychologin und Coachin und bin jetzt eine approbierte Psychotherapeutin.
Aufgabenstellung
Es gibt ein Layout, an das sich angelehnt werden soll.
Die Farb- und Schriftwelt liegt vor, jedoch soll aus dem türkies ein warmer Pink-Rot-Ton werden.
Die Visitenkarte soll für die neu eröffnete Privatpraxis verwendet werden. Im Logo soll die Berufsbezeichnung Psychologische Psychotherapeutin (mit) Schwerpunkt Systemische Therapie stehen.
Neben den Kontaktdaten folgender Text:
Privatpraxis für Psychologische Psychotherapie, Schwerpunkt Systemische Therapie
Für Privatversicherte und Selbstzahlende
Termin nach Vereinbarung
Die Zeile mit der Sprechstunde soll weg.

```html
<!DOCTYPE html>
<html lang="de">
<head>
<meta charset="utf-8">
<title>Visitenkarte Korinna Welse</title>
<link href="https://fonts.googleapis.com/css2?family=Open+Sans:wght@400;600;700&display=swap" rel="stylesheet">
<style>
  :root {
    --bg: #f1f1f1;
    --card: #ffffff;
    --wine: #6b2623;
    --sand: #bdb2a4;
    --sand-light: #d8cdbd;
    --ink: #7d7d7d;
    --rule: #b9b9b9;
  }
  * { margin: 0; padding: 0; box-sizing: border-box; }
  html, body { width: 1200px; height: 894px; overflow: hidden; background: var(--bg); font-family: "Open Sans", sans-serif; }
  .stage { position: relative; width: 1200px; height: 894px; display: flex; align-items: center; justify-content: center; gap: 60px; }
  .card { position: relative; width: 520px; height: 336px; box-shadow: 0 10px 28px rgba(0,0,0,.12); overflow: hidden; }
  .card--front { background: var(--card); }
  .card--back { background: var(--wine); display: flex; flex-direction: column; align-items: center; justify-content: center; }

  .brand { text-align: center; }
  .brand__name { font-weight: 400; font-size: 34px; letter-spacing: 1px; color: var(--sand); line-height: 1; }
  .brand__tagline { margin-top: 10px; font-size: 8.5px; line-height: 1.6; letter-spacing: 2.4px; text-transform: uppercase; color: var(--sand); }
  .card--back .brand__name { font-size: 40px; color: var(--sand-light); }
  .card--back .brand__tagline { color: var(--sand-light); font-size: 9.5px; letter-spacing: 2.8px; }

  .card--front .brand { position: absolute; top: 36px; right: 30px; }

  .profile { position: absolute; left: 30px; top: 132px; width: 260px; }
  .profile__name { font-weight: 700; font-size: 17px; color: var(--sand); letter-spacing: .3px; }
  .profile__title { font-size: 11.5px; color: var(--ink); margin-bottom: 6px; }
  .profile__text { font-size: 11.5px; line-height: 1.45; color: var(--sand); }

  .contact { position: absolute; left: 292px; top: 204px; padding-left: 16px; border-left: 1px solid var(--rule); font-size: 11.5px; color: var(--ink); line-height: 1.5; }
  .contact__address { margin-bottom: 6px; }
  .contact__row { display: flex; align-items: center; gap: 8px; }
  .contact__icon { width: 10px; height: 10px; flex: none; }

  .footer-band { position: absolute; left: 0; bottom: 0; width: 520px; height: 10px; }
</style>
</head>
<body>
<main class="stage">
  <section class="card card--front" aria-label="Vorderseite">
    <div class="brand">
      <div class="brand__name">Korinna Welse</div>
      <div class="brand__tagline">Psychologische Psychotherapeutin<br>Schwerpunkt Systemische Therapie</div>
    </div>

    <div class="profile">
      <div class="profile__name">KORINNA WELSE</div>
      <div class="profile__title">Psychologische Psychotherapeutin</div>
      <p class="profile__text">Privatpraxis für Psychologische<br>Psychotherapie, Schwerpunkt Systemische<br>Therapie. Für Privatversicherte und<br>Selbstzahlende. Termin nach Vereinbarung</p>
    </div>

    <div class="contact">
      <div class="contact__address">Lindenauer Weg 12 . 85699<br>Musterkirchen</div>
      <div class="contact__row">
        <svg class="contact__icon" viewBox="0 0 10 10"><circle cx="5" cy="5" r="5" fill="#6b2623"/><path d="M3 2.6c.4-.3.8-.2 1 .2l.4.8c.1.3 0 .5-.2.7l-.3.2c.3.7.8 1.2 1.5 1.5l.2-.3c.2-.2.4-.3.7-.2l.8.4c.4.2.5.6.2 1-.5.6-1.2.7-2 .3C3.9 6.6 3.3 6 2.8 4.9c-.3-.8-.3-1.6.2-2.3z" fill="#fff"/></svg>
        <span>+49 160 4418270</span>
      </div>
      <div class="contact__row">
        <svg class="contact__icon" viewBox="0 0 10 10"><rect x=".5" y="2" width="9" height="6" fill="none" stroke="#6b2623"/><path d="M.5 2L5 5.5 9.5 2" fill="none" stroke="#6b2623"/></svg>
        <span>kontakt@hmorbachtu.de</span>
      </div>
      <div class="contact__row">
        <svg class="contact__icon" viewBox="0 0 10 10"><circle cx="5" cy="5" r="4.5" fill="none" stroke="#6b2623"/><path d="M.5 5h9M5 .5c-2 2.5-2 6.5 0 9M5 .5c2 2.5 2 6.5 0 9" fill="none" stroke="#6b2623" stroke-width=".8"/></svg>
        <span>www.hmorbachtu.de</span>
      </div>
    </div>

    <svg class="footer-band" viewBox="0 0 520 10" preserveAspectRatio="none">
      <rect width="520" height="10" fill="#6b2623"/>
      <polygon points="150,0 360,0 368,10 142,10" fill="#bdb2a4"/>
    </svg>
  </section>

  <section class="card card--back" aria-label="Rückseite">
    <div class="brand">
      <div class="brand__name">Korinna Welse</div>
      <div class="brand__tagline">Psychologische Psychotherapeutin<br>Schwerpunkt Systemische Therapie</div>
    </div>
  </section>
</main>
</body>
</html>
```